Orvel Prime - Letter Head

My company is a residential and commercial cleaning company , which is located in Abu Dhabi, UAE.
I am looking for a creative letterhead reflects the professional and reflects professionalism and send the feeling of relax and comfort.
The color which will be used it has to be selected carefully in prospective of colors psychological effects, so every color to be used should be for a reason.
Also, reflecting my company colors in an attractive way.
Regarding the information which it should contains, it has to show the address, contacts , telephones an, email address and website.
Also, my company logo is attached
Residential

```html
<!DOCTYPE html>
<html lang="en">
<head>
<meta charset="utf-8">
<title>Orvel Prime – Letterhead</title>
<link rel="stylesheet" href="https://fonts.googleapis.com/css2?family=Kalam:wght@400;700&display=swap">
<style>
  :root {
    --paper: #ffffff;
    --rule: #111111;
    --sun: #fdbf16;
    --leaf: #a6cd38;
    --sky: #0aa3e2;
    --mint: #86cdc4;
    --peach: #f8a54f;
    --navy: #1c4f9c;
    --ink: #1a1a1a;
  }
  html, body {
    margin: 0;
    padding: 0;
    width: 1200px;
    height: 900px;
    overflow: hidden;
    background: var(--paper);
  }
  .letterhead {
    display: block;
    width: 1200px;
    height: 900px;
  }
  .rule { stroke: var(--rule); stroke-width: 2.5; }
  .band-leaf { fill: var(--leaf); }
  .band-sky { fill: var(--sky); }
  .band-sun { fill: var(--sun); }
  .band-mint { fill: var(--mint); }
  .band-peach { fill: var(--peach); }
  .sheet { fill: var(--paper); }
  .contact {
    font-family: "Kalam", cursive;
    fill: var(--ink);
  }
  .contact-address { font-size: 20px; }
  .contact-tel { font-size: 17px; }
  .contact-web { font-size: 16px; }
  .brand-name {
    font-family: "Kalam", cursive;
    font-weight: 700;
    font-size: 30px;
    fill: var(--navy);
  }
  .brand-dot { fill: none; stroke: var(--leaf); stroke-width: 4; }
</style>
</head>
<body>
<svg class="letterhead" viewBox="0 0 1200 900" xmlns="http://www.w3.org/2000/svg">
  <!-- left sidebar -->
  <g class="sidebar">
    <rect class="band-sun" x="0" y="28" width="140" height="855"/>
    <path class="band-sky" d="M0,28 L42,28 C44,330 70,500 110,610 C138,700 136,810 78,883 L0,883 Z"/>
    <path class="band-leaf" d="M0,28 L22,28 C24,330 54,500 100,610 C130,700 128,810 64,883 L0,883 Z"/>
    <path class="sheet" d="M0,110 C8,330 40,500 88,610 C118,700 116,810 50,883 L0,883 Z"/>
    <rect class="band-mint" x="140" y="28" width="18" height="855"/>
    <rect class="band-peach" x="158" y="28" width="32" height="855"/>
    <path class="band-sky" d="M158,620 C152,720 152,820 165,883 L170,883 C160,820 158,720 158,620 Z"/>
    <path class="sheet" d="M165,28 L1200,28 L1200,883 L200,883 C178,883 165,870 165,845 Z"/>
  </g>

  <!-- right edge swoosh -->
  <g class="edge">
    <path class="band-leaf" d="M1085,36 C1160,60 1168,200 1152,360 C1132,560 1144,760 1178,883 L1200,883 L1200,28 L1085,28 Z"/>
    <path class="band-sky" d="M1100,64 C1155,80 1178,160 1166,330 C1150,530 1152,730 1200,860 L1200,28 L1150,28 Z"/>
    <path class="band-peach" d="M1105,28 L1200,28 L1200,883 L1194,883 C1150,740 1136,520 1150,320 C1162,160 1150,70 1105,28 Z"/>
  </g>

  <!-- frame rules -->
  <line class="rule" x1="0" y1="28" x2="1200" y2="28"/>
  <line class="rule" x1="0" y1="883" x2="1200" y2="883"/>

  <!-- contact details -->
  <g class="contact">
    <text class="contact-address" transform="translate(74,155) rotate(-90)" text-anchor="end">Address Line 1</text>
    <text class="contact-address" transform="translate(98,155) rotate(-90)" text-anchor="end">Address Line 2</text>
    <text class="contact-tel" transform="translate(124,145) rotate(-90)" text-anchor="end">Tel : XXXXXXXXXXXX</text>
    <text class="contact-web" transform="translate(155,486) rotate(-90)">Email: xxxxxx@xxx.com&#160;&#160;&#160; www.xxxxxxxxx.com</text>
  </g>

  <!-- brand -->
  <g class="brand">
    <circle class="brand-dot" cx="58" cy="655" r="18"/>
    <text class="brand-name" transform="translate(70,855) rotate(-90)">Orvel Prime</text>
  </g>
</svg>
</body>
</html>
```